Daxholm APP redesign and color change

I am looking for a new design for my app. Please see the attached current design.

Currently, I have a functioning app but the colors and design are awful!
The logo is great but the rest of the app needs a refresh.
(Logo hi res not yet available but will upload soon.)
New colors or anything that is cutting edge.

Basically: It is a secure social media app within a school system where the teachers, students and parents can text, exchange photos, plan curriculum, etc.

I NEED ONLY landing page with a new look!
Looking for one distinct design for the landing page with new look.
The developer will apply this one design towards the rest of the pages/app screens.

Because part of the social media I need the feel and look of what is now the trend. Something that will attract and keep the client(s) interested. I am really leaving all the creative work to the designer and open to any suggestions.
Updates

Target Market(s)

Schools, community, teachers, students, colleges, sport teams

Industry/Entity Type

Non Profit

Font styles to use
Serif
Sans Serif

Colors

Designer to choose colors to be used in the design.

Requirements
Must have
• Sharp, trendy, millennial feel
Nice to have
• Up to designer
Should not have
• Up to designer

```html
<!DOCTYPE html>
<html lang="en">
<head>
<meta charset="utf-8">
<title>Daxholm – Landing</title>
<link rel="stylesheet" href="https://fonts.googleapis.com/css2?family=Open+Sans:wght@600;700&family=Raleway:wght@400;500&display=swap">
<style>
  :root{
    --blue:#0b67e2;
    --blue-photo-a:#3f7fe0;
    --blue-photo-b:#5b93e6;
    --blue-photo-c:#2f6fd8;
    --screen-a:#2b3db0;
    --screen-b:#1f5bd2;
    --orange:#ff9500;
    --white:#ffffff;
    --device:#f4f5f7;
    --device-edge:#d9dce1;
    --ink:#1b1b1b;
  }
  *{box-sizing:border-box;margin:0;padding:0}
  html,body{width:1200px;height:811px;overflow:hidden;background:var(--blue)}
  .landing{position:relative;width:1200px;height:811px;overflow:hidden;background:var(--blue);font-family:"Raleway",sans-serif;color:var(--white)}
  .hero-photo{position:absolute;left:0;top:0;width:1200px;height:468px;
    background:linear-gradient(100deg,var(--blue-photo-b) 0%,var(--blue-photo-a) 40%,var(--blue-photo-c) 70%,var(--blue-photo-b) 100%)}
  .side-photo{position:absolute;left:800px;top:468px;width:400px;height:343px;
    background:linear-gradient(160deg,#6f9fe6 0%,#4c86df 55%,#3a74d6 100%)}
  .brand{position:absolute;left:390px;top:50px;width:400px;text-align:center}
  .brand-mark{display:block;margin:0 auto 38px;width:120px;height:120px;border:6px solid var(--white);border-radius:50%}
  .brand-name{font-family:"Open Sans",sans-serif;font-weight:700;font-size:23px;letter-spacing:.62em;padding-left:.62em;line-height:1}
  .brand-tagline{font-family:"Open Sans",sans-serif;font-weight:600;font-size:13px;letter-spacing:.03em;margin-top:17px}
  .intro{position:absolute;left:428px;top:316px;width:345px;font-size:24.5px;line-height:30px;font-weight:400}
  .btn{position:absolute;left:495px;width:201px;height:55px;display:flex;align-items:center;justify-content:center;font-size:22px;border-radius:3px}
  .btn-login{top:481px;background:var(--orange)}
  .signup-prompt{position:absolute;left:440px;width:300px;top:578px;text-align:center;font-size:19px}
  .btn-signup{top:614px;height:56px;border:3px solid var(--white);border-radius:6px}
  .fine-print{position:absolute;left:433px;top:732px;width:360px;font-family:Arial,sans-serif;font-size:12px;line-height:13px}
  .copyright{position:absolute;left:433px;top:778px;font-family:Arial,sans-serif;font-size:15px}
  .device{position:absolute;left:65px;top:370px;width:295px;height:520px;background:var(--device);border:1px solid var(--device-edge);border-radius:58px}
  .device-btn{position:absolute;width:4px;background:var(--device-edge);border-radius:2px}
  .camera{position:absolute;left:95px;top:36px;width:10px;height:10px;border-radius:50%;background:var(--ink)}
  .speaker{position:absolute;left:125px;top:38px;width:46px;height:5px;border-radius:3px;background:var(--ink)}
  .screen{position:absolute;left:15px;top:72px;width:262px;height:460px;background:linear-gradient(180deg,var(--screen-a) 0%,var(--screen-b) 100%);border:1px solid #0d1a4a}
  .status{display:flex;justify-content:space-between;padding:3px 7px;font-family:Arial,sans-serif;font-size:7px;font-weight:700}
  .screen-brand{position:absolute;left:0;top:183px;width:100%;text-align:center}
  .screen-brand .brand-mark{width:70px;height:70px;border-width:4px;margin-bottom:35px}
  .screen-brand .brand-name{font-size:16px}
  .screen-brand .brand-tagline{font-size:9.5px;margin-top:10px}
</style>
</head>
<body>
<main class="landing">
  <div class="hero-photo" role="img" aria-label="Blue-tinted photo of students and a teacher in a classroom"></div>
  <div class="side-photo" role="img" aria-label="Blue-tinted photo of students talking around a table"></div>

  <header class="brand">
    <span class="brand-mark"></span>
    <div class="brand-name">DAXHOLM</div>
    <div class="brand-tagline">SECURITY THROUGH TRANPARENCY</div>
  </header>

  <p class="intro">Lorem ipsum dolor sit amet, consectetuer adipiscing elit, sed diam nonummy nibh euismod tincidunt ut laoreet</p>

  <div class="device">
    <span class="device-btn" style="left:-4px;top:85px;height:22px"></span>
    <span class="device-btn" style="left:-4px;top:125px;height:40px"></span>
    <span class="device-btn" style="left:-4px;top:175px;height:40px"></span>
    <span class="device-btn" style="right:-4px;top:130px;height:40px"></span>
    <span class="camera"></span>
    <span class="speaker"></span>
    <div class="screen">
      <div class="status"><span>●●●●● ᯤ</span><span>11:47</span><span>86% ▬</span></div>
      <div class="screen-brand">
        <span class="brand-mark"></span>
        <div class="brand-name">DAXHOLM</div>
        <div class="brand-tagline">SECURITY THROUGH TRANPARENCY</div>
      </div>
    </div>
  </div>

  <div class="btn btn-login">LOG IN</div>
  <p class="signup-prompt">Don’t have account?</p>
  <div class="btn btn-signup">Sign Up</div>

  <p class="fine-print">consectetuer adipiscing elit, sed diam nonummy nibh euismod tincidunt ut laoreet dolore magna aliquam erat</p>
  <p class="copyright">© 2107 Lorem ipsum dolor sit amet.</p>
</main>
</body>
</html>
```